4D Hush Little Nest Luxury Ultrasound Billboard

Design a HIGH-END, MODERN billboard for my private prenatal ultrasound studio, 4D Hush Little Nest, located in Pace, Florida.
This billboard will be viewed by drivers traveling at highway speeds, so it must be extremely clean, simple, and readable within 6 seconds.
About My Business
4D Hush Little Nest is a private prenatal ultrasound studio specializing in:
Highest technology 4D/HD Ultrasounds
Early Gender Determination
Pregnancy Confirmation
I have been serving families for nearly 10 years and is known for creating a memorable experience, not just an ultrasound appointment.
Design Style
I DO NOT want:
Flowers
Leaves
Swirls
Glitter
Hearts everywhere
Busy backgrounds
Generic maternity stock graphics
I DO want:
Modern
Luxury
Upscale
Clean
Professional
Eye-catching
Premium medical spa feel
Colors
Use colors from my logo:
LOGO Green ( or a deep green)
Black
White
Soft Gold accents
Images:
Incorporate my professional headshot in a clean, modern way, logo, and the ultrasound images
Text
Keep wording minimal.
Primary Headline ( OPEN TO IDEAS) :
EXAMPLES ( WOULD RATHER SOMETHING MORE CATCHY)
" ADVANCED IMAGING. UNFORGETTABLE MOMENTS"
"MEET YOUR BABY BEFORE BIRTH"
Under headline:
4D Ultrasound • Early Gender • Pregnancy Confirmation
Business Name:
4D Hush Little Nest
Private Prenatal Ultrasound Studio
Phone Number:
850-471-3905
Important
This billboard must be readable in 5–6 seconds from a moving vehicle.
Less text is better.
The phone number and business name must be visible from a distance.
The design should feel like a premium brand that immediately tells expecting parents:
“This is where I go to see my baby.”
Files Provided
Official logo
Headshot
Ultrasound images
Don’t make this look like a medical office billboard.
Make it look like a luxury baby experience billboard. That’s what separates 4D Hush Little Nest from hospitals, OB offices, and all the new studios popping up around you. The emotional connection is what gets moms to book. ❤️
Billboard Size - 10.6” x 36”

```html
<!DOCTYPE html>
<html lang="en">
<head>
<meta charset="utf-8">
<title>4D Hush Little Nest Billboard</title>
<link rel="stylesheet" href="https://fonts.googleapis.com/css2?family=Montserrat:wght@500;600;700&family=Poppins:wght@500&display=swap">
<style>
  :root {
    --backdrop: #2b2b2b;
    --white: #ffffff;
    --gold: #c99b36;
    --sage: #5f726c;
    --photo-tone: #d9d6d0;
  }
  * { margin: 0; padding: 0; box-sizing: border-box; }
  html, body { width: 1200px; height: 900px; overflow: hidden; }
  body {
    background: var(--backdrop);
    display: flex;
    align-items: center;
    justify-content: center;
    font-family: "Montserrat", sans-serif;
  }
  .billboard {
    width: 1120px;
    height: 330px;
    display: flex;
    background: var(--white);
  }
  .brand-panel {
    width: 261px;
    height: 100%;
    background: var(--white);
    display: flex;
    flex-direction: column;
    align-items: center;
    padding-top: 14px;
  }
  .headshot {
    width: 170px;
    height: 222px;
    border-radius: 6px;
    background: linear-gradient(180deg, #ece9e4 0%, var(--photo-tone) 55%, #c7c1b5 100%);
  }
  .brand-name {
    margin-top: 16px;
    font-family: "Montserrat", sans-serif;
    font-weight: 700;
    font-size: 18px;
    color: var(--gold);
    text-align: center;
    line-height: 1.1;
  }
  .brand-tagline {
    margin-top: 8px;
    font-weight: 500;
    font-size: 8.5px;
    letter-spacing: 0.04em;
    color: var(--sage);
  }
  .accent-strip {
    width: 47px;
    height: 100%;
    background: var(--sage);
  }
  .message-panel {
    flex: 1;
    display: flex;
    flex-direction: column;
  }
  .headline-block {
    height: 239px;
    background: var(--gold);
    display: flex;
    flex-direction: column;
    align-items: center;
    justify-content: center;
    padding-top: 18px;
  }
  .headline {
    font-family: "Poppins", sans-serif;
    font-weight: 500;
    font-size: 60px;
    line-height: 1.48;
    letter-spacing: 0.27em;
    color: var(--white);
    text-align: center;
    margin-right: -0.27em;
  }
  .services {
    margin-top: 14px;
    font-weight: 500;
    font-size: 14.5px;
    letter-spacing: 0.03em;
    color: var(--white);
  }
  .contact-band {
    flex: 1;
    background: var(--white);
    display: flex;
    align-items: center;
    justify-content: center;
    gap: 18px;
  }
  .phone-icon { width: 60px; height: 60px; }
  .phone-number {
    font-weight: 700;
    font-size: 66px;
    letter-spacing: 0.03em;
    color: var(--sage);
  }
</style>
</head>
<body>
  <section class="billboard">
    <div class="brand-panel">
      <div class="headshot" role="img" aria-label="Professional headshot of the studio owner holding an ultrasound probe"></div>
      <p class="brand-name">4D Hush Little Nest</p>
      <p class="brand-tagline">PRENATAL ULTRASOUND STUDIO</p>
    </div>
    <div class="accent-strip"></div>
    <div class="message-panel">
      <div class="headline-block">
        <h1 class="headline">MEET YOUR BABY<br>BEFORE BIRTH</h1>
        <p class="services">4D ULTRASOUND • EARLY GENDER • PREGNANCY CONFIRMATION</p>
      </div>
      <div class="contact-band">
        <svg class="phone-icon" viewBox="0 0 60 60" aria-hidden="true">
          <circle cx="30" cy="30" r="27" fill="none" stroke="#5f726c" stroke-width="3"/>
          <path d="M24 14c-3 1-5 4-5 8 0 9 5 19 12 24 2 1 5 1 7-1l2-3-6-5-3 2c-3-3-5-8-6-12l3-1-1-9z" fill="none" stroke="#5f726c" stroke-width="3" stroke-linejoin="round"/>
        </svg>
        <p class="phone-number">850 471 3905</p>
      </div>
    </div>
  </section>
</body>
</html>
```